Dynamic and Revolutionary Training Company Requires Stationery Design Project

We are a training company who deliver training both online and face to face.

We train in:
~ Industry Training: Earth Moving Machinery, Cranes, Work at Heights, Confined Spaces, Elevating Work Platforms, Forklift etc.
~ Food Hygiene / Safety
~ Responsible Service of Alcohol / Gambling

Our company is interested in sourcing stationery designs for:

* Pens
These will be used in classroom training courses but also given away in advertising 'packs'

* Presentation folders
These can be either bi or tri fold cardboard folders. Promotional materials / leaflets will be placed inside these folders and given away in advertising 'packs'

* Letterhead
We need to update our old / outdated letterhead

* Exercise Book Covers
These exercise books will be used by students in our face to face training courses.

* With Compliments Slip
In 100+ envelopes we send each day we currently add a business card. We are now going to add a with with compliments slip with an offer / promotion instead.

* Pull Up Banner
Front of stall display at expos / trade shows.

* Flyers
We would like a template design for a DL sized flyer. We offer training in over 30 courses, so if we had a standard template that could be adapted to each training course we would achieve consistency in advertising.
Flyers would need the same / similar front (with space for a picture) and course information could be placed on the back.

Because of our extensive (and ever expanding) scope of training, certain products (folders, exercise books) will allow us to list some / all our training courses.
Other advertising mediums will obviously only allow us to display our logo and slogan (pens etc).

Please find attached our company logo.
Company slogan -
Updates

Good Morning All,

I apologise for this glaring oversight.

I unfortunately failed to mention that our primary 'business colour' (obviously outside the logo) is blue. 

Traditionally, the blue I refer to is a lightish blue as can be seen on our website banner: www.quorvelskills.edu.au 
We are however moving into a new premises which has navy blue carpet, so we would like to move more towards a navy blue.

We would also like to adjust several sliders, significantly more towards:
* elegant
* personable

And somewhat more towards:
* colourful

Sorry for any inconvenience designers :(

Regards,
Tam

Closing day tomorrow.

Only received designs from 2 designers thus far.

Last chance today to submit designs.............................

Target Market(s)

Employed / unemployed persons looking to upskill, companies / organisations looking for a quality training provider.

Industry/Entity Type

Advertising

Requirements
Must have
• More than happy to be guided by designer.

I would like to see the letterhead also involve a footer - of some sort.

Logo colours are original since company inception so must remain.

Slogan - we do have one, however our advertising has never had it as a major focus.
Nice to have
• Most written correspondence we send via email (statements of attainment, invoices etc) has a Quorvel Training watermark across it.
If possible and it looks appropriate in your opinion, the larger advertising (folders, exercise books) could MAYBE have that as well.

```html
<!DOCTYPE html>
<html lang="en">
<head>
<meta charset="utf-8">
<title>Quorvel Training Stationery</title>
<link href="https://fonts.googleapis.com/css2?family=Arimo&family=Source+Sans+3:wght@400;600;700&display=swap" rel="stylesheet">
<style>
  :root {
    --olive: #aea636;
    --olive-dark: #8f8a2a;
    --ink: #231f20;
    --paper: #ffffff;
    --backdrop: #5a5a57;
    --watermark: #efede3;
  }
  * { box-sizing: border-box; margin: 0; padding: 0; }
  html, body { width: 1200px; height: 849px; overflow: hidden; }
  body { background: var(--backdrop); position: relative; font-family: "Source Sans 3", sans-serif; color: var(--ink); }

  .sheet { position: absolute; background: var(--paper); box-shadow: 0 4px 10px rgba(0,0,0,.35); overflow: hidden; }
  .letterhead { left: 46px; top: 40px; width: 595px; height: 768px; }
  .compliment-slip { left: 576px; top: 400px; width: 579px; height: 270px; }

  .brand { position: absolute; display: flex; flex-direction: column; align-items: flex-start; gap: 8px; }
  .brand-square { width: 46px; height: 46px; background: var(--olive); }
  .brand-name { font-weight: 700; font-size: 12px; line-height: 12px; letter-spacing: .2px; color: var(--ink); text-transform: uppercase; white-space: nowrap; }

  .rule { position: absolute; height: 8px; background: var(--olive); }
  .rule-meta { position: absolute; right: 6px; top: 0; font-size: 5px; line-height: 8px; color: #fff; font-weight: 600; letter-spacing: .2px; white-space: nowrap; }

  .contact { position: absolute; font-size: 7px; line-height: 8.5px; color: #3a3a3a; font-style: normal; }
  .contact .label { color: var(--olive); font-weight: 700; margin-right: 4px; }
  .contact .gap { height: 4px; }
  .contact .web { color: var(--olive-dark); font-weight: 700; }

  .letter { position: absolute; font-family: "Arimo", sans-serif; font-size: 12.5px; line-height: 14px; color: #111; }
  .letter p { white-space: nowrap; }
  .letter-date { left: 49px; top: 170px; }
  .letter-address { left: 49px; top: 213px; }
  .letter-body { left: 49px; top: 311px; width: 545px; }
  .letter-body p { white-space: normal; margin-bottom: 14px; }
  .letter-body .salutation { margin-bottom: 0; }
  .letter-close { left: 49px; top: 505px; }
  .letter-sign { left: 49px; top: 576px; }

  .watermark { position: absolute; left: 284px; top: 548px; width: 300px; font-weight: 700; color: var(--watermark); text-transform: uppercase; line-height: 1; }
  .watermark-square { width: 118px; height: 118px; background: var(--watermark); margin-bottom: 28px; }
  .watermark-name { font-size: 28px; letter-spacing: 1px; white-space: nowrap; }

  .slip-title { position: absolute; right: 31px; bottom: 18px; font-size: 19px; font-weight: 600; color: var(--olive); }
</style>
</head>
<body>

<article class="sheet letterhead">
  <div class="brand" style="left:48px; top:50px;">
    <span class="brand-square"></span>
    <span class="brand-name">Quorvel Training</span>
  </div>
  <address class="contact" style="left:454px; top:47px;">
    PO Box 5170, Marlow Heights,<br>Queensland 4711
    <div class="gap"></div>
    <span class="label">P</span>(07) 4385 2260<br>
    <span class="label">F</span>(07) 4385 2261
    <div class="gap"></div>
    support@quorvelskills.edu.au<br>
    <span class="web">www.quorvelskills.edu.au</span>
  </address>
  <div class="rule" style="left:176px; top:110px; width:371px;">
    <span class="rule-meta">ABN 61 204 338 915 | RTO 40217</span>
  </div>

  <div class="watermark" aria-hidden="true">
    <div class="watermark-square"></div>
    <div class="watermark-name">Quorvel Training</div>
  </div>

  <p class="letter letter-date">September 10, 2012</p>
  <div class="letter letter-address">
    <p>Ms. Carla Whitfield</p>
    <p>Accounts Payable</p>
    <p>The Kitchen Depot</p>
    <p>412 Larkspur Avenue</p>
    <p>Millbrook, CA 68210</p>
  </div>
  <div class="letter letter-body">
    <p class="salutation">Dear Ms. Whitfield,</p>
    <p>It has come to my attention that your company, The Kitchen Depot has been late with paying their invoices for the past three months.</p>
    <p>In order to encourage our customers to pay for their invoices before the due date, we have implemented a discount model where we'll give you 2% off your invoice if you pay us within 10 days of receiving the invoice.</p>
    <p>I hope that everything is going well for you and your company. You are one of our biggest customers, and we appreciate your business. If you have any questions, feel free to contact me at (555) 210-4433.</p>
  </div>
  <p class="letter letter-close">Sincerely,</p>
  <div class="letter letter-sign">
    <p>Ray Delling</p>
    <p>Accounts Receivable</p>
  </div>
</article>

<article class="sheet compliment-slip">
  <div class="brand" style="left:28px; top:22px;">
    <span class="brand-square"></span>
    <span class="brand-name">Quorvel Training</span>
  </div>
  <address class="contact" style="left:457px; top:20px;">
    PO Box 5170, Marlow Heights,<br>Queensland 4711
    <div class="gap"></div>
    <span class="label">P</span>(07) 4385 2260<br>
    <span class="label">F</span>(07) 4385 2261
    <div class="gap"></div>
    support@quorvelskills.edu.au<br>
    <span class="web">www.quorvelskills.edu.au</span>
  </address>
  <div class="rule" style="left:156px; top:84px; width:393px;">
    <span class="rule-meta">ABN 61 204 338 915 | RTO 40217</span>
  </div>
  <p class="slip-title">With Compliment</p>
</article>

</body>
</html>
```